Basic Webdesign for a Financial Site

That's the design right now:

http://www.kurswellenplan.com

We want to keep the base design but make it look more modern and professional.

These are Designs we like:

https://www.boersmalde.de/
http://www.vindaro-shop.com/
http://hochkursmakler.de/
http://www.kolbrecoaching.com/

I use my own WordPress-Theme based on Twitter Bootstrap. I need a PSD and sliced Images (PNG) at the end. Thank you.

Financial

```html
<!DOCTYPE html>
<html lang="en">
<head>
<meta charset="utf-8">
<title>kurswellenplan – Home</title>
<link rel="stylesheet" href="https://fonts.googleapis.com/css2?family=PT+Sans:ital,wght@0,400;0,700;1,400&family=PT+Sans+Narrow:wght@400;700&display=swap">
<style>
  :root {
    --orange: #f0890a;
    --blue: #1466a8;
    --blue-dark: #0d5a97;
    --text: #3a3a3a;
    --muted: #555;
    --line: #d6d6d6;
    --footer: #0d0d0d;
    --white: #ffffff;
  }
  * { box-sizing: border-box; margin: 0; padding: 0; }
  html, body { width: 1026px; height: 1200px; overflow: hidden; }
  body { position: relative; background: var(--white); color: var(--text); font-family: "PT Sans", Arial, sans-serif; }
  a { color: inherit; text-decoration: none; }

  .brand { position: absolute; left: 74px; top: 40px; display: flex; align-items: center; gap: 10px; }
  .brand-mark { width: 34px; height: 34px; background: var(--orange); }
  .brand-name { font-size: 34px; font-weight: 700; color: var(--blue); letter-spacing: -0.5px; }

  .account { position: absolute; right: 74px; top: 35px; font-size: 14px; font-weight: 700; color: #666; }
  .search { position: absolute; right: 74px; top: 76px; width: 193px; height: 29px; border: 1px solid #cfcfcf; border-radius: 3px; padding: 0 28px 0 6px; font: italic 12px/27px "PT Sans", sans-serif; color: #999; }
  .search svg { position: absolute; right: 9px; top: 7px; }

  .main-nav { position: absolute; left: 74px; top: 121px; width: 878px; height: 47px; background: var(--orange); border: 1px solid #e07d05; display: flex; align-items: center; padding-left: 4px; }
  .main-nav a { font-family: "PT Sans Narrow", sans-serif; font-size: 17px; color: var(--white); padding: 0 23px; line-height: 22px; border-left: 1px dotted rgba(255,255,255,.85); }
  .main-nav a:first-child { border-left: none; }

  .hero { position: absolute; left: 74px; top: 168px; width: 878px; height: 341px; overflow: hidden; }
  .hero-photo { position: absolute; inset: 0; background: linear-gradient(100deg, #e6eeec 0%, #d4e2e0 35%, #f1f4f2 55%, #b9c4c6 75%, #e7eaea 100%); }
  .hero-copy { position: absolute; left: 99px; top: 108px; }
  .hero-title { font-family: "PT Sans Narrow", sans-serif; font-weight: 700; font-size: 30px; color: var(--blue); letter-spacing: 0.2px; }
  .hero-sub { margin-top: 4px; font-size: 19px; color: #333; letter-spacing: 0.3px; }
  .hero-text { margin-top: 10px; font-size: 14px; line-height: 22px; color: #333; width: 360px; }
  .slider-arrow { position: absolute; top: 141px; width: 46px; height: 46px; border-radius: 50%; background: rgba(170,170,170,.55); display: flex; align-items: center; justify-content: center; }
  .slider-arrow.prev { left: 15px; }
  .slider-arrow.next { right: 15px; }

  .feature { position: absolute; top: 541px; width: 250px; text-align: center; }
  .feature-badge { width: 126px; height: 126px; margin: 0 auto; border-radius: 50%; background: radial-gradient(circle at 50% 35%, #ffffff 0%, #f1f1f1 55%, #d9d9d9 100%); box-shadow: 0 4px 10px rgba(0,0,0,.12); display: flex; align-items: center; justify-content: center; }
  .feature-title { margin-top: 14px; font-size: 18px; font-weight: 700; color: #333; }
  .feature-text { margin-top: 5px; font-size: 13px; line-height: 18.5px; color: var(--muted); }

  .section-title { position: absolute; font-size: 21px; color: #333; }

  .post { position: absolute; left: 73px; width: 540px; height: 106px; }
  .post-thumb { position: absolute; left: 0; top: 0; width: 116px; height: 106px; border: 1px solid var(--line); background: linear-gradient(160deg, #ffffff 0%, #f2f4f2 60%, #e3ebe3 100%); }
  .post-body { position: absolute; left: 133px; top: 0; width: 410px; }
  .post-title { font-size: 15.5px; color: var(--blue); }
  .post-text { margin-top: 5px; font-size: 12px; line-height: 18px; color: #333; }
  .post-meta { margin-top: 6px; display: flex; align-items: center; gap: 16px; font-size: 11px; font-style: italic; color: #444; }
  .share { font-style: normal; font-size: 11px; font-weight: 700; color: #333; border: 1px solid #ddd; border-radius: 3px; background: linear-gradient(#fff, #ececec); padding: 1px 7px; }
  .share.like { color: #3b5998; font-weight: 400; background: #eef1f7; border-color: #c5cde0; }

  .about-video { position: absolute; left: 694px; top: 834px; width: 256px; height: 132px; background: linear-gradient(180deg, #8f9393 0%, #7f8585 100%); }
  .play { position: absolute; left: 108px; top: 46px; }
  .about-lead { position: absolute; left: 696px; top: 981px; width: 256px; font-size: 13px; font-weight: 700; line-height: 18px; color: #333; }
  .about-text { position: absolute; left: 696px; top: 1022px; width: 256px; font-size: 12px; line-height: 18px; color: var(--muted); }

  .site-footer { position: absolute; left: 0; top: 1111px; width: 1026px; height: 89px; background: var(--footer); color: var(--white); }
  .footer-links { position: absolute; left: 74px; top: 23px; font-size: 12px; }
  .copyright { position: absolute; left: 74px; top: 51px; font-size: 12px; }
  .social { position: absolute; right: 73px; top: 28px; display: flex; gap: 11px; }
  .social span { width: 30px; height: 30px; display: block; }
  .social .fb { background: #3b5a9a; }
  .social .tw { background: #2aa4e0; }
  .social .rss { background: #f26a1b; }
  .social .yt { background: #d8232a; }
</style>
</head>
<body>

<header>
  <a class="brand" href="#"><span class="brand-mark"></span><span class="brand-name">kurswellenplan</span></a>
  <div class="account"><a href="#">LOGIN</a> | <a href="#">REGISTER</a></div>
  <div class="search">Search..
    <svg width="12" height="12" viewBox="0 0 12 12"><circle cx="5" cy="5" r="3.8" fill="none" stroke="#999" stroke-width="1.6"/><line x1="7.8" y1="7.8" x2="11" y2="11" stroke="#999" stroke-width="1.8"/></svg>
  </div>
</header>

<nav class="main-nav">
  <a href="#">HOME</a><a href="#">ABOUT US</a><a href="#">BOOK</a><a href="#">BLOG</a><a href="#">PRODUCTS</a><a href="#">COACHING</a><a href="#">USEFUL INFO</a>
</nav>

<section class="hero">
  <div class="hero-photo" role="img" aria-label="Bright glass office corridor with hands holding a tablet showing a stock chart"></div>
  <div class="hero-copy">
    <h1 class="hero-title">GENERAL MARKET COMMENTARY</h1>
    <p class="hero-sub">DON'T BUY ANYMORE IN-STORE SERVICE</p>
    <p class="hero-text">Jerta baditaut onsequser untur magni dolores eoquie volup tate msequi nesciunt. Voluptatem accusantium dolorem.</p>
  </div>
  <a class="slider-arrow prev" href="#"><svg width="12" height="20" viewBox="0 0 12 20"><polyline points="10,1 2,10 10,19" fill="none" stroke="#fff" stroke-width="1.5"/></svg></a>
  <a class="slider-arrow next" href="#"><svg width="12" height="20" viewBox="0 0 12 20"><polyline points="2,1 10,10 2,19" fill="none" stroke="#fff" stroke-width="1.5"/></svg></a>
</section>

<section class="features">
  <div class="feature" style="left:103px">
    <div class="feature-badge">
      <svg width="70" height="54" viewBox="0 0 70 54"><rect x="2" y="2" width="66" height="46" fill="none" stroke="#1466a8" stroke-width="4"/><rect x="12" y="12" width="46" height="4" fill="#1466a8"/><rect x="12" y="21" width="46" height="4" fill="#1466a8"/><rect x="12" y="30" width="30" height="4" fill="#1466a8"/><path d="M50 30 v14 l-4 -3 v8 h16 v-10 l-8 -3 v-6z" fill="#1466a8"/></svg>
    </div>
    <h2 class="feature-title">Our Features</h2>
    <p class="feature-text">Lorem ipsum dolor sit amet adipis ing elit.Morbi ut elipsum tristique acc Pellentesque habitant morbi.</p>
  </div>
  <div class="feature" style="left:381px">
    <div class="feature-badge">
      <svg width="56" height="56" viewBox="0 0 56 56"><circle cx="28" cy="28" r="27" fill="#1466a8"/><text x="28" y="40" text-anchor="middle" font-family="PT Sans, sans-serif" font-weight="700" font-size="34" fill="#fff">$</text></svg>
    </div>
    <h2 class="feature-title">Fixed Pricing</h2>
    <p class="feature-text">Lorem ipsum dolor sit amet adipis ing elit.Morbi ut elipsum tristique acc Pellentesque habitant morbi.</p>
  </div>
  <div class="feature" style="left:676px">
    <div class="feature-badge">
      <svg width="68" height="60" viewBox="0 0 68 60"><circle cx="46" cy="14" r="11" fill="#1466a8"/><path d="M34 46 c0-14 8-20 16-20 c10 0 16 8 16 18 v2z" fill="#1466a8"/><circle cx="24" cy="20" r="13" fill="#1466a8" stroke="#f3f3f3" stroke-width="3"/><path d="M2 58 c0-16 10-24 22-24 s22 8 22 24z" fill="#1466a8" stroke="#f3f3f3" stroke-width="3"/></svg>
    </div>
    <h2 class="feature-title">Coaching Clients</h2>
    <p class="feature-text">Lorem ipsum dolor sit amet adipis ing elit.Morbi ut elipsum tristique acc Pellentesque habitant morbi.</p>
  </div>
</section>

<section class="recent-blog">
  <h2 class="section-title" style="left:73px; top:790px">Recent Blog</h2>
  <article class="post" style="top:831px">
    <div class="post-thumb" role="img" aria-label="Candlestick price chart with trend lines"></div>
    <div class="post-body">
      <h3 class="post-title">Suspendisse eu erat quam. Vivamus porttitor eros quis.</h3>
      <p class="post-text">Suspendisse eu erat quam. Vivamus porttitor eros quis nisi lacinia sed interdum uam a orci quis nisi sagittis sagittis. Etiam adipiscing, justo quis feugiat.Suspend amus porttitor eros quis nisi lacinia sed interdum lorem vulputate.</p>
      <div class="post-meta">Posted on 02 June, 2013 <span class="share">Follow</span><span class="share like">Like</span></div>
    </div>
  </article>
  <article class="post" style="top:955px">
    <div class="post-thumb" role="img" aria-label="Line chart of a rising price"></div>
    <div class="post-body">
      <h3 class="post-title">Suspendisse eu erat quam. Vivamus porttitor eros quis.</h3>
      <p class="post-text">Suspendisse eu erat quam. Vivamus porttitor eros quis nisi lacinia sed interdum uam a orci quis nisi sagittis sagittis. Etiam adipiscing, justo quis feugiat.Suspend amus porttitor eros quis nisi lacinia sed interdum lorem vulputate.</p>
      <div class="post-meta">Posted on 02 June, 2013 <span class="share">Follow</span><span class="share like">Like</span></div>
    </div>
  </article>
</section>

<aside class="about">
  <h2 class="section-title" style="left:695px; top:790px">About us</h2>
  <div class="about-video" role="img" aria-label="Video still of a candlestick chart with moving averages">
    <svg class="play" width="40" height="40" viewBox="0 0 40 40"><circle cx="20" cy="20" r="18" fill="#2b2b2b" stroke="#fff" stroke-width="2.5"/><polygon points="15,11 29,20 15,29" fill="#fff"/></svg>
  </div>
  <p class="about-lead">There are many variations anythin emba rss true generator on Internet.</p>
  <p class="about-text">Nunc venenatis lacinia lacus quis vulputate. Susp endisse imperdiet leo sed urna molestie.</p>
</aside>

<footer class="site-footer">
  <div class="footer-links"><a href="#">Home</a> | <a href="#">About Us</a> | <a href="#">Book</a> | <a href="#">Blog</a> | <a href="#">Products</a> | <a href="#">Coaching</a> | <a href="#">Useful</a></div>
  <p class="copyright">Copyrights 2013. All Rights Reserved.</p>
  <div class="social"><span class="fb"></span><span class="tw"></span><span class="rss"></span><span class="yt"></span></div>
</footer>

</body>
</html>
```